Home page graphic design only (NOT WEBSITE DESIGN)

I require a home page to be designed for my new website.
I DO NOT REQUIRE to build a website. We are a rug company specialising in alpaca wool. It is targeted at the high end of the market and hence the graphics of our page requires to reflect this. Our current page is as per attachment and I think it is too basic.
Updates

Target Market(s)

Extremly high net worth individuals where luxury is a requirement

Requirements
Must have
• show of style, luxury, uniqueness. Prefer having bright images.
Nice to have
• a highly sofisticated roomscape where the focus in the rug. See attachment as an example
Should not have
• Not sure

```html
<!DOCTYPE html>
<html lang="en">
<head>
<meta charset="utf-8">
<title>Maison Velours – Home</title>
<link rel="stylesheet" href="https://fonts.googleapis.com/css2?family=Arimo:wght@400;500&family=Cormorant+Garamond:wght@500&family=Satisfy&display=swap">
<style>
  :root {
    --black: #040404;
    --gold: #f5b92e;
    --gold-soft: #d8b35c;
    --paper: #f6f5f0;
    --ink: #111111;
    --white: #ffffff;
    --footer-text: #c9c9c9;
    --icon: #4a4a4a;
  }
  * { margin: 0; padding: 0; box-sizing: border-box; }
  html, body { width: 1200px; height: 703px; overflow: hidden; background: var(--black); }
  .page { position: relative; width: 1200px; height: 703px; font-family: "Arimo", Arial, sans-serif; }

  .site-header { position: absolute; left: 0; top: 0; width: 1200px; height: 57px; background: var(--black); }
  .brand { position: absolute; left: 41px; top: 12px; font-family: "Cormorant Garamond", Georgia, serif; font-weight: 500; font-size: 25px; color: var(--gold-soft); letter-spacing: 0.5px; }
  .main-nav a { position: absolute; top: 9px; font-size: 12.5px; color: var(--white); text-decoration: none; }
  .main-nav a.active { color: var(--gold); }
  .nav-caret { position: absolute; left: 408px; top: 15px; width: 0; height: 0; border-left: 3px solid transparent; border-right: 3px solid transparent; border-top: 4px solid var(--white); }
  .brand-dot { position: absolute; left: 1138px; top: 14px; width: 28px; height: 28px; border-radius: 50%; background: var(--gold); }

  .intro { position: absolute; left: 0; top: 57px; width: 506px; height: 603px; background: var(--paper); text-align: center; }
  .intro-title { position: absolute; left: 0; width: 506px; top: 100px; font-family: "Cormorant Garamond", Georgia, serif; font-weight: 500; font-size: 70px; line-height: 1; color: var(--gold); white-space: nowrap; }
  .tagline { position: absolute; left: 0; width: 506px; top: 250px; font-family: "Satisfy", cursive; font-size: 23px; line-height: 48px; color: var(--ink); }
  .tagline strong { font-weight: 700; font-size: 25px; }
  .established { position: absolute; left: 0; width: 506px; top: 389px; font-size: 9.5px; letter-spacing: 1.2px; color: var(--ink); }
  .regions { position: absolute; left: 0; width: 506px; top: 413px; font-size: 13px; font-weight: 500; letter-spacing: 1.1px; color: var(--ink); }
  .company, .abn { position: absolute; left: 0; width: 506px; font-size: 9.5px; letter-spacing: 1.2px; color: var(--ink); }
  .company { top: 439px; }
  .abn { top: 462px; }

  .roomscape { position: absolute; left: 506px; top: 57px; width: 694px; height: 605px;
    background:
      linear-gradient(160deg, transparent 0 55%, rgba(240,170,110,0.55) 75%, rgba(245,185,130,0.7) 100%),
      linear-gradient(180deg, #b8b8bb 0%, #9a9a9d 25%, #8a8781 40%, #aaa194 65%, #b4ab9d 100%); }

  .site-footer { position: absolute; left: 0; top: 662px; width: 1200px; height: 41px; background: var(--black); }
  .copyright { position: absolute; left: 30px; top: 14px; font-size: 9.8px; color: var(--footer-text); white-space: nowrap; }
  .social { position: absolute; top: 11px; width: 19px; height: 19px; border-radius: 50%; background: var(--icon); }
</style>
</head>
<body>
<div class="page">
  <header class="site-header">
    <div class="brand">Maison Velours</div>
    <nav class="main-nav">
      <a class="active" href="#" style="left:251px">Home</a>
      <a href="#" style="left:322px">Collections</a>
      <span class="nav-caret"></span>
      <a href="#" style="left:422px">Our Story</a>
      <a href="#" style="left:510px">About us</a>
      <a href="#" style="left:598px">FAQ</a>
      <a href="#" style="left:662px">Publications</a>
      <a href="#" style="left:767px">News &amp; Events</a>
      <a href="#" style="left:890px">Contact us</a>
    </nav>
    <span class="brand-dot"></span>
  </header>

  <section class="intro">
    <h1 class="intro-title">Maison Velours</h1>
    <p class="tagline">Exquisite luxury carpeting and area rugs made<br>from pure <strong>Peruvian alpaca</strong></p>
    <p class="established">Established in 1988</p>
    <p class="regions">AUSTRALIA ~ USA ~ EUROPE ~ UK ~ ASIA ~ UAE</p>
    <p class="company">Maison Velours Pty Ltd</p>
    <p class="abn">ABN 12 345 678 901</p>
  </section>

  <div class="roomscape" role="img" aria-label="Rendered living room with grey tufted sofas, white side tables, glass coffee table and a large textured beige alpaca rug on a warm timber floor"></div>

  <footer class="site-footer">
    <p class="copyright">Copyright @2020 Maison Velours - Australia - Head Office - Suite 5 / Unit 12 – 88 Willow Bend Road;Willow Bend VIC 3000</p>
    <span class="social" style="left:1037px"></span>
    <span class="social" style="left:1066px"></span>
    <span class="social" style="left:1095px"></span>
    <span class="social" style="left:1124px"></span>
    <span class="social" style="left:1153px"></span>
  </footer>
</div>
</body>
</html>
```